Bramble Gate Stud

We have an existing website for our Thoroughbred Breeding and racing farm in The Plains Virginia we would like to improve it Our Web address is www.bramblegatestud.example
We also have a facebook page and a twitter account for our Stallion Moonlark whom we would like to Spotlight on our website. More Pictures and Info Available.
We would also like to work with the designer we choose to create our brochure for our farm. as well as some promotional material for our stallion Moonlark.
Please see the following competitor website, www.fenwaldacres.example we like the conservative and classic feel of this site design.
Updates

Project Deadline Extended
Reason: We want to give everyone a chance to make some changes we feel there have been some great ideas thus far. Thank you

Project Deadline Extended
Reason: Waiting on a few design changes from designers to come in.

Target Market(s)

Thoroughbred Breeders and Trainers

Industry/Entity Type

Conservative

Font styles to use
Sans Serif

Colors
3277b5
85abd2
0555a3
ffffff

Requirements
Must have
• Please see current website @ www.bramblegatestud.example

```html
<!DOCTYPE html>
<html lang="en">
<head>
<meta charset="utf-8">
<title>Bramble Gate Stud</title>
<link href="https://fonts.googleapis.com/css2?family=Open+Sans:wght@400;600;700;800&display=swap" rel="stylesheet">
<style>
:root{
  --navy:#0a1f3a;
  --navy-deep:#071629;
  --blue:#0555a3;
  --blue-mid:#3277b5;
  --blue-light:#85abd2;
  --white:#ffffff;
  --grey-bg:#f0f1f3;
  --text:#6b7078;
  --line:#d5d9de;
}
*{box-sizing:border-box;margin:0;padding:0}
html,body{width:768px;height:1200px;overflow:hidden}
body{font-family:"Open Sans",Arial,sans-serif;background:var(--white);color:var(--text);position:relative}
.site-header{position:absolute;top:0;left:0;width:768px;height:86px;background:rgba(7,22,41,.92);z-index:2;display:flex;align-items:center;justify-content:space-between;padding:0 24px 0 40px}
.brand{display:flex;align-items:center;gap:8px;color:var(--white);font-weight:700;font-size:15px;letter-spacing:.2px;white-space:nowrap}
.brand-dot{width:12px;height:12px;border-radius:50%;background:var(--blue-mid)}
.main-nav{display:flex;gap:4px;white-space:nowrap}
.main-nav a{color:var(--white);text-decoration:none;font-size:9.5px;font-weight:600;padding:10px 9px;text-transform:uppercase}
.main-nav a.active{background:var(--blue)}
.hero{position:absolute;top:0;left:0;width:768px;height:440px;background:linear-gradient(160deg,#9fb3a0 0%,#6e7f5e 35%,#4a3c2e 70%,#2b2520 100%)}
.hero-copy{position:absolute;top:252px;left:234px;width:400px;text-align:center;color:var(--white)}
.hero-copy h1{font-size:21px;font-weight:800;line-height:1.2;text-transform:uppercase}
.hero-copy p{font-size:8px;line-height:1.5;margin:8px 20px 0;text-transform:uppercase}
.btn{display:inline-block;background:var(--blue);color:var(--white);font-size:9px;font-weight:700;text-transform:uppercase;padding:9px 18px;text-decoration:none}
.hero-copy .btn{margin-top:14px;padding:10px 20px}
.hero-dots{position:absolute;top:404px;left:648px;display:flex;gap:6px}
.hero-dots span{width:9px;height:9px;border-radius:50%;border:1px solid var(--white)}
.hero-dots span.on{background:var(--white)}
.features{position:absolute;top:470px;left:48px;width:672px;display:flex;gap:24px}
.feature{width:208px}
.feature h2{color:var(--blue-mid);font-size:16px;font-weight:700;text-transform:uppercase;margin-bottom:12px}
.feature .photo{height:118px}
.feature h3{font-size:11px;font-weight:700;color:#333;text-transform:uppercase;margin:14px 0 6px}
.feature p{font-size:8.5px;line-height:1.55;margin-bottom:14px}
.photo-mares{background:linear-gradient(180deg,#b9c6cf 0%,#7a9a4f 45%,#c9a35f 100%)}
.photo-stallion{background:linear-gradient(180deg,#8aa3b5 0%,#6d8a52 55%,#5a4a38 100%)}
.photo-training{background:linear-gradient(180deg,#6a7f95 0%,#3f6fa8 50%,#5a3d2a 100%)}
.info-band{position:absolute;top:755px;left:0;width:768px;height:333px;background:var(--grey-bg);padding:28px 48px;display:flex;gap:40px}
.about{width:430px}
.about h2,.contact h2{color:var(--blue-mid);font-size:16px;font-weight:700;text-transform:uppercase;margin-bottom:12px}
.about p{font-size:8.5px;line-height:1.65;margin-bottom:10px}
.about .btn{margin-top:10px}
.contact{width:202px}
.contact address{font-style:normal;font-size:8.5px;line-height:1.6;margin-bottom:10px}
.field{display:block;width:100%;height:22px;background:var(--white);border:1px solid var(--line);font-size:8px;color:#999;padding:5px 7px;margin-bottom:7px}
.field.message{height:52px}
.site-footer{position:absolute;top:1088px;left:0;width:768px;height:112px;background:var(--navy-deep);text-align:center;padding-top:16px}
.footer-nav{display:flex;justify-content:center;gap:16px}
.footer-nav a{color:var(--blue-light);font-size:8.5px;text-decoration:none;text-transform:uppercase}
.copyright{color:var(--white);font-size:8px;margin-top:10px;letter-spacing:.3px}
.social{display:flex;justify-content:center;gap:8px;margin-top:14px}
.social span{width:16px;height:16px;border-radius:50%;background:#8a96a6}
</style>
</head>
<body>
<div class="hero" role="img" aria-label="Thoroughbred racehorses with jockeys galloping on a track"></div>
<header class="site-header">
  <div class="brand"><span class="brand-dot"></span>Bramble Gate Stud</div>
  <nav class="main-nav">
    <a class="active" href="#">Home</a><a href="#">Stallions</a><a href="#">Mares and Foals</a><a href="#">Horses in Training</a><a href="#">About Our Facility</a><a href="#">Contact</a>
  </nav>
</header>
<section class="hero-copy">
  <h1>Thoroughbred Breeding<br>and Racing at it's Best!</h1>
  <p>Generations of careful breeding, patient training and quiet country care in the heart of Virginia hunt country.</p>
  <a class="btn" href="#">Know More</a>
</section>
<div class="hero-dots"><span class="on"></span><span></span><span></span><span></span></div>

<section class="features">
  <article class="feature">
    <h2>Mares and Foals</h2>
    <div class="photo photo-mares" role="img" aria-label="Mares and foals grazing in a paddock"></div>
    <h3>Boarding</h3>
    <p>With over 400 acres of beautiful land, large 40 acre field turn out, and an experienced foaling team, we are your mare.</p>
    <a class="btn" href="#">Read More</a>
  </article>
  <article class="feature">
    <h2>Stallions</h2>
    <div class="photo photo-stallion" role="img" aria-label="Bay stallion standing on grass"></div>
    <h3>Moonlark</h3>
    <p>With over 400 acres of beautiful land, large 40 acre field turn out, and an experienced foaling team, we are your mare.</p>
    <a class="btn" href="#">Read More</a>
  </article>
  <article class="feature">
    <h2>Horses in Training</h2>
    <div class="photo photo-training" role="img" aria-label="Racehorse in training with jockey"></div>
    <h3>Training</h3>
    <p>With over 400 acres of beautiful land, large 40 acre field turn out, and an experienced foaling team, we are your mare.</p>
    <a class="btn" href="#">Read More</a>
  </article>
</section>

<section class="info-band">
  <div class="about">
    <h2>Who We Are</h2>
    <p>Bramble Gate Stud is a family run thoroughbred breeding, rest and training yard in Alder Springs, Virginia. With many years of experience with young stock, we keep our herd small, which lets us give close and personal attention to every single horse.</p>
    <p>Bramble Gate Stud offers board for weanlings, yearlings, and two-year-olds in training. Services include quality care, round the clock checks and close attention to the daily routine of all horses. Learn more about Bramble Gate Stud.</p>
    <a class="btn" href="#">Read More</a>
  </div>
  <div class="contact">
    <h2>Contact Us</h2>
    <address>Tel: (555) 014-2200<br>120 Bramble Gate Lane<br>Alder Springs, VA 20000</address>
    <span class="field">Name</span>
    <span class="field">Email</span>
    <span class="field message">Message</span>
    <a class="btn" href="#">Submit</a>
  </div>
</section>

<footer class="site-footer">
  <nav class="footer-nav">
    <a href="#">Home</a><a href="#">Stallions</a><a href="#">Mares and Foals</a><a href="#">Horses in Training</a><a href="#">About Our Facility</a><a href="#">Contact</a>
  </nav>
  <p class="copyright">ALL RIGHTS RESERVED. COPYRIGHT © 2014</p>
  <div class="social"><span></span><span></span><span></span><span></span></div>
</footer>
</body>
</html>
```